Stationary for Hair Cosmetic company

We mainly sell hair thickening products www.morvello-wellform.de/morvello-hair/ Hair thickening products are a smart and easy solution for thinning hair for both men and women. We sell very information oriented in an honest undramatic manner.

We would like to see a decent color and style that is suitable for men and women. It shall be rather modern with a vintage spin as our own product (Morvello Bottle). Please use our logo (attatched).

Please bias your design to the bottle. To give you an idea: Chalk design like http://de.pixaverum.com/id/48213597 or one-color watercolor like http://de.pixaverum.com/id/63925180 is appreciated but not necessary.

Good but rejected designs will get compensation.

Target Market(s)

Wide range in demographics: age 20-55; 45% male, 55% women; issues with hair loss; self-conscious

Industry/Entity Type

Hair

Colors
3377b5
33a6d7
32b7a4
cbdf83
fbf289
fee18a
f9bb93
f05157

Requirements
Must have
• trustworthiness
Nice to have
• Chalk design like http://de.pixaverum.com/id/48213597 or one-color watercolor like http://de.pixaverum.com/id/63925180 is appreciated but not necessary

```html
<!DOCTYPE html>
<html lang="en">
<head>
<meta charset="utf-8">
<title>Morvello Hair – Stationery</title>
<link href="https://fonts.googleapis.com/css2?family=Michroma&family=Montserrat:wght@400;500;600&display=swap" rel="stylesheet">
<style>
  :root {
    --stage: #e2e3e5;
    --paper: #ffffff;
    --coral: #f05157;
    --charcoal: #3c3c3e;
    --charcoal-deep: #2f2f31;
    --ink: #1d1d1f;
    --muted: #6b6b6e;
    --mist: #d9d9db;
    --brand: "Michroma", sans-serif;
    --body: "Montserrat", sans-serif;
  }
  * { box-sizing: border-box; margin: 0; padding: 0; }
  html, body { width: 1200px; height: 640px; overflow: hidden; background: var(--stage); }
  .canvas { position: relative; width: 1200px; height: 640px; }
  .piece { position: absolute; background: var(--paper); overflow: hidden; box-shadow: 0 2px 6px rgba(0,0,0,.18); }
  .piece svg.art { position: absolute; inset: 0; width: 100%; height: 100%; }
  .mark { position: absolute; border-radius: 50%; background: var(--coral); }
  .wordmark { position: absolute; font-family: var(--brand); color: var(--ink); white-space: nowrap; letter-spacing: .02em; }

  /* Letterhead */
  .letterhead { left: 30px; top: 16px; width: 314px; height: 442px; }
  .letterhead .mark { left: 36px; top: 10px; width: 48px; height: 48px; }
  .letterhead .wordmark { left: 20px; top: 68px; font-size: 7px; }
  .letterhead .rule { position: absolute; left: 98px; right: 0; top: 78px; border-top: 1px solid #8a8a8c; }
  .letterhead .contacts { position: absolute; left: 218px; top: 34px; font-family: var(--body); font-size: 4.6px; font-weight: 600; color: var(--ink); line-height: 7.4px; list-style: none; }
  .contacts .dot { display: inline-block; width: 5px; height: 5px; border-radius: 50%; background: var(--coral); margin-right: 3px; vertical-align: -1px; }

  /* Folder spread */
  .folder-spread { left: 440px; top: 20px; width: 360px; height: 252px; background: var(--charcoal); }
  .panel { position: absolute; top: 0; width: 180px; height: 252px; }
  .panel-back { left: 0; }
  .panel-front { left: 180px; }
  .pattern { position: absolute; inset: 0; background: linear-gradient(160deg, var(--charcoal) 0%, var(--charcoal-deep) 100%); }
  .seal { position: absolute; left: 72px; top: 196px; width: 36px; height: 40px; border-radius: 50%; background: #e9e9ea; }
  .back-contacts { position: absolute; left: 0; right: 0; bottom: 6px; display: flex; justify-content: center; gap: 8px; font-family: var(--body); font-size: 3.6px; color: #cfcfd1; list-style: none; white-space: nowrap; }
  .back-contacts .dot { width: 3.5px; height: 3.5px; margin-right: 2px; }
  .panel-front .mark { left: 124px; top: 22px; width: 40px; height: 40px; }
  .panel-front .wordmark { right: 12px; top: 70px; font-size: 6.4px; }

  /* Folder front (large) */
  .folder-front { left: 860px; top: 262px; width: 300px; height: 350px; background: var(--charcoal); }
  .folder-front .mark { left: 200px; top: 14px; width: 72px; height: 72px; }
  .folder-front .wordmark { right: 22px; top: 98px; font-size: 10.5px; }

  /* Business cards */
  .card-back { left: 212px; top: 484px; width: 218px; height: 130px; }
  .card-back .watermark { position: absolute; left: 2px; top: 2px; width: 94px; height: 126px; border-radius: 50%; background: var(--mist); }
  .card-back .name { position: absolute; left: 114px; top: 26px; font-family: var(--brand); font-size: 8px; color: var(--coral); letter-spacing: .04em; white-space: nowrap; }
  .card-back .role { position: absolute; left: 114px; top: 38px; font-family: var(--body); font-size: 5px; color: var(--muted); }
  .card-back .contacts { position: absolute; left: 114px; top: 82px; font-family: var(--body); font-size: 6px; color: var(--ink); line-height: 9.5px; list-style: none; }
  .card-back .contacts .dot { width: 6px; height: 6px; margin-right: 3px; }

  .card-front { left: 458px; top: 414px; width: 123px; height: 200px; }
  .card-front .mark { left: 22px; top: 50px; width: 80px; height: 80px; }
  .card-front .wordmark { left: 0; right: 0; text-align: center; top: 146px; font-size: 9px; }
</style>
</head>
<body>
<main class="canvas">

  <!-- Letterhead -->
  <section class="piece letterhead" aria-label="Letterhead">
    <svg class="art" viewBox="0 0 314 442" preserveAspectRatio="none" aria-hidden="true">
      <path d="M0 412 C80 396 160 400 220 414 C260 424 290 420 314 404 V442 H0 Z" fill="var(--coral)"/>
      <path d="M0 396 C80 380 170 388 230 406 C255 414 272 418 284 420 C260 417 240 412 220 407 C160 393 80 390 0 404 Z" fill="var(--ink)"/>
    </svg>
    <span class="mark" aria-hidden="true"></span>
    <span class="wordmark">Morvello Hair</span>
    <span class="rule"></span>
    <ul class="contacts">
      <li><span class="dot"></span>051 862 3947</li>
      <li><span class="dot"></span>051 862 3947</li>
      <li><span class="dot"></span>hello@morvellohair.com</li>
      <li>PO Box 1185, Hallow Street</li>
      <li>Kestrelmoor, Country Name</li>
    </ul>
  </section>

  <!-- Folder spread -->
  <section class="piece folder-spread" aria-label="Presentation folder, outside spread">
    <div class="panel panel-back">
      <div class="pattern" role="img" aria-label="Dark charcoal engraved hair-strand pattern"></div>
      <span class="seal" role="img" aria-label="Light emblem area"></span>
      <ul class="back-contacts contacts">
        <li><span class="dot"></span>051 862 3947</li>
        <li><span class="dot"></span>hello@morvellohair.com</li>
        <li><span class="dot"></span>PO Box 1185 Hallow</li>
      </ul>
    </div>
    <div class="panel panel-front">
      <div class="pattern" role="img" aria-label="Dark charcoal engraved hair-strand pattern"></div>
      <svg class="art" viewBox="0 0 180 252" preserveAspectRatio="none" aria-hidden="true">
        <path d="M0 0 H180 V140 C110 136 35 100 0 18 Z" fill="var(--coral)"/>
        <path d="M0 0 H180 V130 C110 126 35 92 0 8 Z" fill="var(--paper)"/>
      </svg>
      <span class="mark" aria-hidden="true"></span>
      <span class="wordmark">Morvello Hair</span>
    </div>
  </section>

  <!-- Folder front -->
  <section class="piece folder-front" aria-label="Presentation folder, front cover">
    <div class="pattern" role="img" aria-label="Dark charcoal engraved hair-strand pattern"></div>
    <svg class="art" viewBox="0 0 300 350" preserveAspectRatio="none" aria-hidden="true">
      <path d="M0 0 H300 V196 C190 196 60 150 0 56 Z" fill="var(--coral)"/>
      <path d="M0 0 H300 V184 C190 184 60 140 0 44 Z" fill="var(--paper)"/>
    </svg>
    <span class="mark" aria-hidden="true"></span>
    <span class="wordmark">Morvello Hair</span>
  </section>

  <!-- Business card, back -->
  <section class="piece card-back" aria-label="Business card, contact side">
    <span class="watermark" role="img" aria-label="Faint grey emblem area"></span>
    <p class="name">Daniel Harwick</p>
    <p class="role">Director</p>
    <ul class="contacts">
      <li><span class="dot"></span>07715392608</li>
      <li><span class="dot"></span>07715392608</li>
      <li><span class="dot"></span>info@morvellohair.com</li>
      <li><span class="dot"></span>www.morvellohair.com</li>
    </ul>
  </section>

  <!-- Business card, front -->
  <section class="piece card-front" aria-label="Business card, brand side">
    <span class="mark" aria-hidden="true"></span>
    <span class="wordmark">Morvello Hair</span>
  </section>

</main>
</body>
</html>
```